Business Stationery - New Business card design

We are looking for some new business stationery, including business cards (double sided), compliment slips & letterheads for our offices in the UK, Ireland, North Carolina (US) & our Holdings company.

We are open to all ideas; however we are ideally looking for something that does not look corporate.

Our website is www.talvonahumancapital.example – this is the style of branding that we are currently using.

Here is some of the information that should be included;

Business Cards

Front
Logo
Name – Desmond Varrow
Job Title - Director
Direct line number - +353 (0)1 468 2071
Office number - +353 (0)1 482 6150
Email address – d.varrow@talvonahc.example
Website address – www.talvonahumancapital.example

Back
Logo
‘Specialists in IT Recruitment’
LinkedIn – Talvona Human Capital
Twitter - @talvonahire
An image included – possibly ‘Image 1’ attached?

Letterheads & Compliment slips

UK (A4 size)
Logo
Phone numbers for the various offices;
London: +44 (0)20 7961 3327
Belfast: +44 (0)28 9037 6615
Dublin: +353 (0)1 482 6150
Raleigh, NC: +1 919 642 1357
Address: 2nd Floor, 118 Marlowe Street, London W1C 4PJ
Email: info@talvonahc.example
Website: www.talvonahumancapital.example
Social media icons for LinkedIn & Twitter
Talvona Human Capital Registered in England & Wales No. 6815337 VAT No. 871342609

Ireland (A4 size)
Logo
Address: 4-7 Corran Street, Dublin 2 D02 KX58, Ireland
Email: info@talvonahc.example
Talvona Human Capital (Ireland) Registered in Ireland No. 624903 VAT No. 7182635KK

USA (letter size)

Logo
Address: 542 N. Pellam Street, Raleigh, North Carolina 27605, United States
Email: info@talvonahc.example
Talvona Human Capital Inc. Registered in the State of North Carolina No. 2640917

Holdings (A4 size)

Logo
Address: 58 Fenwick Street, Belfast BT27JD
Email: info@talvonahc.example
Talvona Human Capital (Holdings) Ltd Registered in Northern Ireland No. NI583076

Target Market(s)

IT Professionals

Industry/Entity Type

It Professional

Contact Information for Business Card

Front
Logo
Name – Desmond Varrow
Job Title - Director

Back
Logo
Twitter - @talvonahire

```html
<!DOCTYPE html>
<html lang="en">
<head>
<meta charset="utf-8">
<title>Talvona Human Capital – Letterhead</title>
<link rel="stylesheet" href="https://fonts.googleapis.com/css2?family=Open+Sans:wght@400;600&family=Arimo:wght@400&display=swap">
<style>
  :root {
    --brand-blue: #1c4f9c;
    --brand-green: #5aa624;
    --ink: #4a4a4a;
    --ink-dark: #222;
    --paper: #ffffff;
    --backdrop: #e9e9e9;
  }
  * { box-sizing: border-box; margin: 0; padding: 0; }
  html, body { width: 1040px; height: 1200px; overflow: hidden; background: var(--backdrop); }
  .letterhead {
    position: absolute; left: 54px; top: 0; width: 932px; height: 1200px;
    background: var(--paper); font-family: "Open Sans", sans-serif; color: var(--ink);
  }
  .brand {
    position: absolute; top: 44px; left: 0; right: 0; text-align: center;
    font-family: "Open Sans", sans-serif; font-weight: 600; color: var(--brand-blue);
  }
  .brand-name { font-size: 40px; letter-spacing: 1px; line-height: 1; }
  .brand-row { display: inline-flex; align-items: center; gap: 12px; }
  .brand-dot { width: 16px; height: 16px; border-radius: 50%; background: var(--brand-green); }
  .body-copy { position: absolute; left: 87px; width: 753px; font-size: 14.5px; }
  .issue-date { top: 218px; }
  .recipient { top: 255px; line-height: 18px; }
  .salutation { top: 359px; }
  .paragraph { line-height: 27px; text-align: justify; }
  .p1 { top: 414px; }
  .p2 { top: 576px; }
  .p3 { top: 684px; }
  .closing { top: 818px; }
  .signatory-name { top: 895px; font-size: 19px; font-weight: 600; color: #333; }
  .signatory-role { top: 927px; }
  .footer-rule { position: absolute; left: 0; right: 0; height: 3px; background: var(--brand-blue); }
  .rule-top { top: 1041px; }
  .rule-bottom { top: 1151px; }
  .contact { position: absolute; font-family: "Arimo", sans-serif; font-size: 17px; color: var(--ink-dark);
    display: flex; align-items: center; gap: 5px; white-space: nowrap; }
  .contact svg { width: 21px; height: 21px; flex: none; }
  .registration { position: absolute; top: 1161px; left: 84px; font-family: "Arimo", sans-serif;
    font-size: 17px; color: var(--ink-dark); word-spacing: 1px; white-space: nowrap; }
  .registration .gap { display: inline-block; width: 22px; }
</style>
</head>
<body>
<svg width="0" height="0" style="position:absolute">
  <defs>
    <symbol id="icon-phone" viewBox="0 0 20 20">
      <circle cx="10" cy="10" r="10" fill="#5aa624"/>
      <path d="M6.6 5.2l1.6-.4 1.1 2.5-1 .9c.5 1.3 1.5 2.3 2.8 2.9l.9-1 2.5 1.1-.4 1.6c-.2.6-.8.9-1.4.8C9.600 13 7 10.400 6.4 7c-.1-.7.200-1.600.2-1.800z" fill="#fff"/>
    </symbol>
    <symbol id="icon-mail" viewBox="0 0 20 20">
      <circle cx="10" cy="10" r="10" fill="#5aa624"/>
      <rect x="5" y="6.5" width="10" height="7" rx="1" fill="#fff"/>
      <path d="M5.3 7l4.7 3.6L14.7 7" stroke="#5aa624" stroke-width="1.1" fill="none"/>
    </symbol>
    <symbol id="icon-web" viewBox="0 0 20 20">
      <circle cx="10" cy="10" r="10" fill="#5aa624"/>
      <circle cx="10" cy="10" r="5" fill="none" stroke="#fff" stroke-width="1.2"/>
      <ellipse cx="10" cy="10" rx="2.2" ry="5" fill="none" stroke="#fff" stroke-width="1"/>
      <path d="M5 10h10" stroke="#fff" stroke-width="1"/>
    </symbol>
    <symbol id="icon-pin" viewBox="0 0 20 20">
      <circle cx="10" cy="10" r="10" fill="#5aa624"/>
      <path d="M10 4.5a3.6 3.6 0 0 0-3.6 3.6c0 2.700 3.600 7 3.600 7s3.600-4.300 3.600-7A3.600 3.600 0 0 0 10 4.500z" fill="#fff"/>
      <circle cx="10" cy="8.1" r="1.3" fill="#5aa624"/>
    </symbol>
  </defs>
</svg>

<main class="letterhead">
  <header class="brand">
    <div class="brand-row">
      <span class="brand-name">Talvona Human Capital</span>
      <span class="brand-dot"></span>
    </div>
  </header>

  <p class="body-copy issue-date">Issuing Date: May 5, 2018</p>
  <p class="body-copy recipient">Name Of Employee Mr. XYZABC<br>Address of Employee<br>Address Line 2 etc..</p>
  <p class="body-copy salutation">Dear Mr.XYZABC</p>

  <p class="body-copy paragraph p1">Lorem Ipsum has been the industry's standard dummy text ever since the 1500s, when an unknown printer took a galley of type and scrambled it to make a type specimen book. It has survived not only five centuries, but also the leap into electronic typesetting, remaining essentially unchanged. It was popularised in the 1960s with the release of Marquet sheets containing Lorem Ipsum passages, and more recently with desktop publishing software like Quillset Composer including versions of Lorem Ipsum.</p>
  <p class="body-copy paragraph p2">Lorem Ipsum is simply dummy text of the printing and typesetting industry. Lorem Ipsum has been the industry's standard dummy text ever since the 1500s, when an unknown printer took a galley of type and scrambled it to make a type specimen book.</p>
  <p class="body-copy paragraph p3">It has survived not only five centuries, but also the leap into electronic typesetting, remaining essentially unchanged. It was popularised in the 1960s with the release of Marquet sheets containing Lorem IpsumIpsum passages.</p>

  <p class="body-copy closing">Yours Sincerely</p>
  <p class="body-copy signatory-name">Corwin Ashdale</p>
  <p class="body-copy signatory-role">Managing Director</p>

  <footer>
    <div class="footer-rule rule-top"></div>
    <div class="contact" style="left:58px;top:1057px"><svg><use href="#icon-phone"/></svg>London: +44 (0)20 7961 3327</div>
    <div class="contact" style="left:58px;top:1083px"><svg><use href="#icon-phone"/></svg>Belfast: +44 (0)28 9037 6615</div>
    <div class="contact" style="left:58px;top:1111px"><svg><use href="#icon-pin"/></svg>2nd Floor, 118 Marlowe Street, London W1C 4PJ</div>
    <div class="contact" style="left:327px;top:1057px"><svg><use href="#icon-phone"/></svg>Dublin: +353 (0)1 482 6150</div>
    <div class="contact" style="left:327px;top:1083px"><svg><use href="#icon-phone"/></svg>Raleigh, NC: +1 919 642 1357</div>
    <div class="contact" style="left:604px;top:1059px"><svg><use href="#icon-mail"/></svg>info@talvonahc.example</div>
    <div class="contact" style="left:604px;top:1081px;font-size:15.5px"><svg><use href="#icon-web"/></svg>www.talvonahumancapital.example</div>
    <div class="footer-rule rule-bottom"></div>
    <p class="registration">Talvona Human Capital Registered in England &amp; Wales No. 6815337<span class="gap"></span>VAT No. 871342609</p>
  </footer>
</main>
</body>
</html>
```